Our Kitchen Pantry is an online food market place that connects foodies who make or grow great food with

We would like a 1/2 A4 page size flyer in landscape to promote our new business. We would like to encourage new home foodies to sign up for a membership on our website www.ourkitchenpantrynz.co.nz and we would like customers who are looking for great food in their local community to search our website for their closest home foodie and support a neighbour who is growing or producing creative food locally

Target Market(s)

Creative food lovers

Industry/Entity Type

Landscape

Colors
acd037
f78f20
33b8a4

Requirements
Must have
• Food images and look groovy
• Must be easy to read and stand out on a notice board
• Website address www.ourkitchenpantrynz.co.nz
Nice to have
• We wish to use this flyer in multiple locations and wish to put in different contact details prior to printing

```html
<!DOCTYPE html>
<html lang="en">
<head>
<meta charset="utf-8">
<title>Our Kitchen Pantry – Flyer</title>
<link rel="stylesheet" href="https://fonts.googleapis.com/css2?family=Montserrat:wght@700&family=PT+Serif&family=Arimo:wght@700&family=Oswald:wght@700&display=swap">
<style>
  :root {
    --backdrop: #e9e6e1;
    --paper: #ffffff;
    --orange: #f7901e;
    --mint: #5fe39c;
    --leaf: #3fae2a;
    --grass: #3cb40a;
    --lime: #b6e61e;
    --bark: #3a1f12;
    --kraft: #c8a57c;
    --white: #ffffff;
  }
  * { margin: 0; padding: 0; box-sizing: border-box; }
  html, body { width: 1200px; height: 900px; overflow: hidden; background: var(--backdrop); }
  .flyer {
    position: absolute; left: 28px; top: 48px; width: 1144px; height: 804px;
    background: var(--paper); overflow: hidden;
  }
  .hero-photo {
    position: absolute; left: 0; top: 0; width: 600px; height: 640px;
    background:
      linear-gradient(90deg, rgba(255,255,255,0) 55%, #fff 96%),
      radial-gradient(ellipse at 45% 75%, #9bc46a 0%, rgba(155,196,106,0) 30%),
      radial-gradient(ellipse at 18% 85%, #d5382c 0%, rgba(213,56,44,0) 18%),
      linear-gradient(180deg, #eef0ef 0%, #dfe2e1 45%, #cfc3b6 100%);
  }
  .band { position: absolute; left: 0; top: 0; width: 1144px; height: 804px; }
  .headline {
    position: absolute; right: 58px; top: 36px; width: 700px; text-align: right;
    font-family: "Montserrat", sans-serif; font-weight: 700; font-size: 32px;
    line-height: 44px; text-transform: uppercase; color: var(--orange); letter-spacing: 0.3px;
  }
  .headline .accent { color: var(--mint); }
  .pitch {
    position: absolute; left: 426px; width: 290px; text-align: center;
    font-family: "PT Serif", serif; font-size: 19px; line-height: 25px; color: var(--leaf);
  }
  .pitch--seller { top: 212px; }
  .pitch--buyer { top: 356px; }
  .brand {
    position: absolute; left: 790px; top: 200px; width: 320px;
    display: flex; align-items: center; gap: 14px;
  }
  .brand-dot { width: 40px; height: 40px; border-radius: 50%; background: var(--kraft); flex: none; }
  .brand-name {
    font-family: "Oswald", sans-serif; font-weight: 700; font-size: 50px; line-height: 52px;
    text-transform: uppercase; color: var(--bark);
  }
  .contact {
    position: absolute; right: 48px; top: 660px; text-align: right;
    font-family: "Arimo", sans-serif; font-weight: 700;
  }
  .contact-lead { font-size: 28px; color: var(--lime); line-height: 38px; }
  .contact-url { font-size: 29px; color: var(--white); line-height: 40px; text-transform: uppercase; }
</style>
</head>
<body>
  <main class="flyer">
    <div class="hero-photo" role="img" aria-label="Photo of a smiling cook in a striped apron tossing a fresh salad with tomatoes and cucumber in a bright kitchen"></div>

    <svg class="band" viewBox="0 0 1144 804" aria-hidden="true">
      <path d="M0 582 C 260 640, 520 620, 760 548 C 920 500, 1060 420, 1144 300 L 1144 318 C 1060 440, 920 520, 760 566 C 520 636, 260 656, 0 600 Z" fill="var(--bark)"/>
      <path d="M0 598 C 260 654, 520 634, 760 564 C 920 518, 1060 438, 1144 316 L 1144 804 L 0 804 Z" fill="var(--grass)"/>
    </svg>

    <h1 class="headline">
      Be part of our exciting <span class="accent">new online food marketplace</span> connecting foodies in your local community
    </h1>

    <p class="pitch pitch--seller">As a foodie you can sell your beautiful home produced or home grown produce on our marketplace website</p>
    <p class="pitch pitch--buyer">As a food lover you can purchase lovingly grown or prepared food and support your local foodie community while keeping your food miles low</p>

    <div class="brand">
      <span class="brand-dot"></span>
      <span class="brand-name">Our Kitchen<br>Pantry</span>
    </div>

    <div class="contact">
      <p class="contact-lead">For more information go to:</p>
      <p class="contact-url">www.ourkitchenpantrynz.co.nz</p>
    </div>
  </main>
</body>
</html>
```